Kestwell Finanz AG needs web design

We need a website for a Swiss company: Kestwell Finanz AG. We offer our customers financial services such as advice and funds. We also have an interest rate calculator that we want to link to via a button on the website.

We are looking for a black and gold design. (Background: Black, Accents: Gold and White)
The design should convey security and growth. We have uploaded our logo in the attachment.
Font from the logo: Trajan Pro Regular

```html
<!DOCTYPE html>
<html lang="en">
<head>
<meta charset="utf-8">
<title>Kestwell Finanz AG</title>
<link rel="stylesheet" href="https://fonts.googleapis.com/css2?family=Cinzel:wght@400;600&family=Lato:wght@400;700&display=swap">
<style>
:root{
  --black:#0b0b0b;
  --ink:#161412;
  --gold:#c9a45c;
  --gold-light:#e6cd8f;
  --gold-dark:#9a7635;
  --white:#ffffff;
  --paper:#f6f4f0;
  --grey:#8a857d;
  --text-dark:#3a3632;
}
*{box-sizing:border-box;margin:0;padding:0}
html,body{width:1200px;height:3724px;overflow:hidden}
body{background:var(--black);color:var(--white);font-family:"Lato",Arial,sans-serif;position:relative}
.serif{font-family:"Cinzel",Georgia,serif}
.btn{display:inline-block;font-family:"Cinzel",Georgia,serif;font-size:15px;letter-spacing:1px;color:#1a1408;
  background:linear-gradient(180deg,var(--gold-light),var(--gold) 55%,var(--gold-dark));padding:12px 30px;border-radius:20px;text-decoration:none;text-transform:uppercase}
.gold-rule{position:absolute;background:var(--gold)}

/* header */
.site-header{position:absolute;top:0;left:0;width:1200px;height:110px;z-index:5}
.brand{position:absolute;left:28px;top:18px;display:flex;align-items:center;gap:10px}
.brand-mark{width:14px;height:14px;background:var(--gold)}
.brand-name{font-family:"Cinzel",Georgia,serif;font-size:20px;color:var(--gold);line-height:1.1;width:150px}
.topbar{position:absolute;right:40px;top:14px;font-size:13px;color:var(--white);display:flex;gap:28px;align-items:center}
.topbar span{display:flex;align-items:center;gap:6px}
.main-nav{position:absolute;right:0;top:38px;height:44px;width:700px;background:linear-gradient(90deg,rgba(201,164,92,.35),var(--gold) 30%,var(--gold-dark));
  clip-path:polygon(40px 0,100% 0,100% 100%,0 100%);display:flex;align-items:center;justify-content:flex-end;gap:28px;padding-right:40px}
.main-nav a{color:#fff;font-size:13px;text-decoration:none}
.main-nav a.active{color:#1a1408;font-weight:700}

/* hero */
.hero{position:absolute;top:0;left:0;width:1200px;height:660px;background:#141210;clip-path:polygon(0 0,100% 0,100% 86%,62% 100%,30% 92%,0 100%)}
.hero-photo{position:absolute;inset:0;background:linear-gradient(90deg,#0c0b0a 0%,#1e1b17 35%,#5d4a36 60%,#7a6752 78%,#3a3027 100%)}
.hero-copy{position:absolute;left:150px;top:230px;width:520px}
.hero-copy h1{font-family:"Cinzel",Georgia,serif;font-weight:400;font-size:40px;color:var(--gold-light);line-height:1}
.hero-copy h2{font-family:"Lato",Arial,sans-serif;font-weight:700;font-size:34px;line-height:1.2;margin-top:8px}
.hero-copy p{font-size:14px;color:#ddd;margin:18px 0 22px;width:380px;line-height:1.5}

/* about */
.about{position:absolute;top:660px;left:0;width:1200px;height:660px;background:var(--black)}
.about-photo{position:absolute;left:240px;top:120px;width:320px;height:300px;background:linear-gradient(135deg,#5b6f85,#c8ccd1 50%,#3b4048)}
.about-badge{position:absolute;left:120px;top:360px;font-family:"Cinzel",Georgia,serif;font-size:32px;color:var(--gold);width:300px;line-height:1.1}
.about-copy{position:absolute;left:630px;top:130px;width:380px}
.eyebrow{font-family:"Cinzel",Georgia,serif;color:var(--gold);font-size:15px}
.about-copy h3{font-family:"Cinzel",Georgia,serif;font-weight:400;color:var(--gold-light);font-size:28px;margin:6px 0 18px}
.about-copy p{font-size:13px;line-height:1.6;color:#ccc;margin-bottom:14px}

/* services */
.services{position:absolute;top:1320px;left:0;width:1200px;height:520px;background:linear-gradient(180deg,#fff,var(--paper) 70%,#d9d6d2);clip-path:polygon(0 6%,50% 0,100% 6%,100% 100%,0 100%)}
.section-title{font-family:"Cinzel",Georgia,serif;font-weight:400;font-size:32px;text-align:center;color:var(--gold);text-transform:uppercase}
.section-intro{text-align:center;font-size:13px;color:var(--grey);margin-top:10px}
.service-grid{position:absolute;top:200px;left:340px;width:540px;display:flex;gap:40px}
.service{width:250px;text-align:left}
.service-icon{width:84px;height:84px;border-radius:50%;background:var(--black);border:3px solid var(--gold);margin:0 0 18px 60px;display:flex;align-items:center;justify-content:center}
.service h4{font-family:"Cinzel",Georgia,serif;font-weight:400;color:var(--gold-dark);font-size:19px;margin-bottom:8px}
.service p{font-size:12.5px;color:var(--text-dark);line-height:1.55;margin-bottom:14px}
.service .btn{font-size:13px;padding:8px 22px}

/* products */
.products{position:absolute;top:1840px;left:0;width:1200px;height:640px;background:linear-gradient(90deg,#050505,#1c1a17 60%,#0c0b0a)}
.products-frame{position:absolute;left:120px;top:110px;width:1070px;height:440px;border:1px solid var(--gold);border-right:none}
.products h3{position:absolute;left:180px;top:85px;background:var(--black);padding:0 16px;font-family:"Cinzel",Georgia,serif;font-weight:400;color:var(--gold-light);font-size:34px}
.products-intro{position:absolute;left:190px;top:150px;font-size:13px;color:#bbb}
.product-list{position:absolute;left:230px;top:240px;width:420px;list-style:none}
.product-list li{font-family:"Cinzel",Georgia,serif;font-size:14px;color:var(--gold-light);padding:16px 40px;border-bottom:1px solid rgba(201,164,92,.4);background:rgba(255,255,255,.03)}
.product-list li:first-child{border-top:1px solid rgba(201,164,92,.4)}
.products-photo{position:absolute;left:650px;top:190px;width:330px;height:330px;background:radial-gradient(circle at 60% 55%,#b89a5e,#4d4434 55%,#1b1a18)}

/* partners */
.partners{position:absolute;top:2480px;left:0;width:1200px;height:560px;background:#fff;clip-path:polygon(0 0,40% 6%,100% 0,100% 100%,0 100%)}
.partners .section-title{padding-top:90px}
.partner-grid{position:absolute;top:200px;left:145px;display:flex;gap:18px}
.partner{width:220px}
.partner-photo{height:200px}
.partner h5{font-family:"Cinzel",Georgia,serif;font-weight:400;font-size:17px;color:var(--text-dark);margin-top:12px}

/* calculator */
.calculator{position:absolute;top:3000px;left:0;width:1200px;height:420px;background:linear-gradient(180deg,#e7ddd0,#a78c63 40%,#3a2f22 80%,#0b0b0b);clip-path:polygon(0 12%,50% 0,100% 12%,100% 100%,0 100%)}
.calculator-copy{position:absolute;top:170px;width:100%;text-align:center}
.calculator-copy h3{font-family:"Cinzel",Georgia,serif;font-weight:400;font-size:34px;color:var(--white)}
.calculator-copy p{font-size:13px;color:#eee;margin:10px auto 20px;width:340px;line-height:1.5}

/* footer */
.site-footer{position:absolute;top:3420px;left:0;width:1200px;height:304px;background:var(--black)}
.footer-brand{position:absolute;left:90px;top:90px;font-family:"Cinzel",Georgia,serif;color:var(--gold);font-size:30px;width:260px;line-height:1.15;text-align:center}
.footer-contact{position:absolute;right:60px;top:110px;display:flex;gap:26px;font-size:13px}
.footer-contact span{display:flex;gap:6px;align-items:center}
.newsletter{position:absolute;right:60px;top:150px;width:500px}
.newsletter h6{font-family:"Cinzel",Georgia,serif;font-weight:400;font-size:17px;color:var(--gold);text-align:right;margin-bottom:10px}
.newsletter form{display:flex;gap:8px}
.newsletter .field{flex:1;height:36px;background:#fff;border-radius:18px;color:#888;font-size:12px;padding:10px 16px}
.newsletter .btn{padding:9px 24px;font-size:13px}
.copyright{position:absolute;right:60px;bottom:44px;font-size:11px;color:var(--grey)}
</style>
</head>
<body>

<section class="hero">
  <div class="hero-photo" role="img" aria-label="Advisers reviewing figures on a tablet in a bright office"></div>
  <div class="hero-copy">
    <h1>WE ARE EXPERT IN</h1>
    <h2>Financial Advice And<br>Funds Services.</h2>
    <p>The fund is an equity allocation strategy that invests exclusively in Swiss blue-chip firms.</p>
    <a class="btn" href="#calculator">Interest Rate Calculator</a>
  </div>
</section>

<header class="site-header">
  <div class="brand"><span class="brand-mark"></span><span class="brand-name">Kestwell Finanz AG</span></div>
  <div class="topbar">
    <span><svg width="12" height="12" viewBox="0 0 24 24" fill="#c9a45c"><path d="M6.6 10.8a15 15 0 0 0 6.6 6.6l2.2-2.2c.3-.3.7-.4 1-.2 1.1.4 2.3.6 3.6.6.6 0 1 .4 1 1V20c0 .6-.4 1-1 1A17 17 0 0 1 3 4c0-.6.4-1 1-1h3.5c.6 0 1 .4 1 1 0 1.3.2 2.5.6 3.6.1.3 0 .7-.2 1z"/></svg>+41 44 555 0192</span>
    <span><svg width="13" height="10" viewBox="0 0 24 18" fill="none" stroke="#c9a45c" stroke-width="2"><rect x="1" y="1" width="22" height="16"/><path d="M1 1l11 9 11-9"/></svg>info@kestwellfinanz.ch</span>
  </div>
  <nav class="main-nav">
    <a class="active" href="#">Home</a><a href="#">About Us</a><a href="#">Services</a><a href="#">Investment Products</a><a href="#">Partners</a><a href="#">Insights</a><a href="#">Contact Us</a>
  </nav>
</header>

<section class="about">
  <div class="gold-rule" style="left:150px;top:0;width:1px;height:270px"></div>
  <div class="gold-rule" style="left:150px;top:270px;width:90px;height:1px"></div>
  <div class="gold-rule" style="left:1070px;top:300px;width:1px;height:360px"></div>
  <div class="gold-rule" style="left:1010px;top:300px;width:60px;height:1px"></div>
  <div class="about-photo" role="img" aria-label="Hands holding a tablet showing financial charts"></div>
  <div class="about-badge">Kestwell Finanz AG</div>
  <div class="about-copy">
    <div class="eyebrow">About Us</div>
    <h3>Kestwell Finanz AG</h3>
    <p>We have been advising private and institutional clients since 1998, building portfolios with patience, discipline and a clear focus on long-term security and steady growth.</p>
    <p>Our team combines Swiss precision with global market insight. Every mandate is reviewed regularly, every risk is explained openly, and every decision is taken with your goals in mind.</p>
    <a class="btn" href="#">Read More</a>
  </div>
</section>

<section class="services">
  <div class="gold-rule" style="left:120px;top:120px;width:960px;height:1px"></div>
  <div class="gold-rule" style="left:120px;top:120px;width:1px;height:330px"></div>
  <div class="gold-rule" style="left:1080px;top:120px;width:1px;height:330px"></div>
  <div style="padding-top:100px">
    <h3 class="section-title"><span style="background:#fff;padding:0 18px">Services We Offer</span></h3>
    <p class="section-intro">We offer tailored solutions that protect your wealth and help it grow.</p>
  </div>
  <div class="service-grid">
    <div class="service">
      <div class="service-icon"><svg width="40" height="40" viewBox="0 0 40 40" fill="none" stroke="#c9a45c" stroke-width="2"><circle cx="20" cy="20" r="14"/><path d="M20 11v18M16 15h6a3 3 0 0 1 0 6h-4a3 3 0 0 0 0 6h6"/></svg></div>
      <h4>Asset Management</h4>
      <p>We manage diversified portfolios with a disciplined process, clear reporting and a strong focus on capital preservation.</p>
      <a class="btn" href="#">Know More</a>
    </div>
    <div class="service">
      <div class="service-icon"><svg width="40" height="40" viewBox="0 0 40 40" fill="none" stroke="#c9a45c" stroke-width="2"><path d="M8 30h24M11 30V22M18 30V16M25 30V19M32 30V10"/><path d="M9 18l8-7 7 4 9-8"/></svg></div>
      <h4>Investment Advice</h4>
      <p>Independent advice for every stage of life, from first investments to complex family wealth and succession plans.</p>
      <a class="btn" href="#">Know More</a>
    </div>
  </div>
</section>

<section class="products">
  <div class="products-frame"></div>
  <h3>Investment Products</h3>
  <p class="products-intro">We offer our investment products across Swiss and global markets.</p>
  <ul class="product-list">
    <li>AMC</li>
    <li>Equity Funds</li>
    <li>Total Return Funds</li>
  </ul>
  <div class="products-photo" role="img" aria-label="Stacks of gold coins on a hexagon-patterned surface"></div>
</section>

<section class="partners">
  <div class="gold-rule" style="left:120px;top:110px;width:960px;height:1px"></div>
  <div class="gold-rule" style="left:120px;top:110px;width:1px;height:70px"></div>
  <div class="gold-rule" style="left:1080px;top:110px;width:1px;height:70px"></div>
  <h3 class="section-title"><span style="background:#fff;padding:0 18px">Partners We Offer</span></h3>
  <p class="section-intro">Trusted specialists who support our clients beyond investments.</p>
  <div class="partner-grid">
    <div class="partner"><div class="partner-photo" role="img" aria-label="Model house with a red roof beside coins" style="background:linear-gradient(135deg,#c9c2b8,#8e3b2e 55%,#5d5a55)"></div><h5>Real Estate</h5></div>
    <div class="partner"><div class="partner-photo" role="img" aria-label="Glass jar filled with coins for retirement savings" style="background:linear-gradient(135deg,#d8d2c5,#a59272 55%,#6b5e49)"></div><h5>Pensions</h5></div>
    <div class="partner"><div class="partner-photo" role="img" aria-label="Clock beside stacked coins and tax blocks" style="background:linear-gradient(135deg,#e5e0d8,#b08f57 55%,#5c4a30)"></div><h5>Taxes</h5></div>
    <div class="partner"><div class="partner-photo" role="img" aria-label="Testament document with pen on a desk" style="background:linear-gradient(135deg,#e8d9c2,#b4542f 55%,#6a3b22)"></div><h5>Wills &amp; Inheritance</h5></div>
  </div>
</section>

<section class="calculator" id="calculator" role="img" aria-label="Desk with laptop and calculator in warm light">
  <div class="calculator-copy">
    <h3>Interest Rate Calculator</h3>
    <p>Plan your next step with confidence and see how your savings can grow over time.</p>
    <a class="btn" href="#">Interest Rate Calculator</a>
  </div>
</section>

<footer class="site-footer">
  <div class="footer-brand">Kestwell Finanz AG</div>
  <div class="footer-contact">
    <span><svg width="12" height="12" viewBox="0 0 24 24" fill="#c9a45c"><path d="M6.6 10.8a15 15 0 0 0 6.6 6.6l2.2-2.2c.3-.3.7-.4 1-.2 1.1.4 2.3.6 3.6.6.6 0 1 .4 1 1V20c0 .6-.4 1-1 1A17 17 0 0 1 3 4c0-.6.4-1 1-1h3.5c.6 0 1 .4 1 1 0 1.3.2 2.5.6 3.6.1.3 0 .7-.2 1z"/></svg>+41 44 555 0192</span>
    <span><svg width="13" height="10" viewBox="0 0 24 18" fill="none" stroke="#c9a45c" stroke-width="2"><rect x="1" y="1" width="22" height="16"/><path d="M1 1l11 9 11-9"/></svg>info@kestwellfinanz.ch</span>
  </div>
  <div class="newsletter">
    <h6>Newsletter Signup</h6>
    <form><div class="field">Enter Email</div><span class="btn">Subscribe</span></form>
  </div>
  <p class="copyright">© 2024 Kestwell Finanz AG. All rights reserved.</p>
</footer>

</body>
</html>
```